Adult Coloring Book Cover Design

We need a cover created for our New Coloring book.
The title needs to be clear and visible on the front of book. Preferable easy to read when the cover is minimized to about 2 inches on screen. The Full title of the book is:
Quiet Meadow Coloring Book: The Gentle Grownup Coloring Book for Her Patient Wanderers

This is a Religious Based coloring book. Attached are some images from inside the book, feel free to add them to the cover design. We like color!
Looking for something that is attention grabbing but not too over the top.
front cover is 8.5in width and 11in length. I will need all PSD files in order to make any necessary changes once awarded.

```html
<!DOCTYPE html>
<html lang="en">
<head>
<meta charset="utf-8">
<title>Quiet Meadow Coloring Book</title>
<link rel="stylesheet" href="https://fonts.googleapis.com/css2?family=Fredoka:wght@700&family=Dancing+Script:wght@700&display=swap">
<style>
  :root {
    --plum: #3b1538;
    --plum-deep: #2e0f2c;
    --teal: #1fae98;
    --crimson: #e0354f;
    --paper: #ffffff;
    --title-red: #d8304b;
  }
  html, body {
    margin: 0;
    padding: 0;
    overflow: hidden;
    background: var(--plum);
  }
  .cover {
    position: relative;
    width: 848px;
    height: 1200px;
    background: var(--plum);
    overflow: hidden;
  }
  .pattern-field {
    position: absolute;
    left: 31px;
    top: 31px;
    width: 786px;
    height: 1043px;
    border: 3px solid var(--plum-deep);
    box-sizing: border-box;
    background:
      radial-gradient(ellipse at 50% 50%, rgba(255,255,255,0.55) 0%, rgba(255,255,255,0) 55%),
      linear-gradient(135deg, var(--teal) 0%, #8fcfc2 30%, var(--crimson) 55%, #7fcbbd 78%, var(--teal) 100%);
  }
  .title-panel {
    position: absolute;
    left: 193px;
    top: 188px;
    width: 466px;
    height: 683px;
    box-sizing: border-box;
    background: var(--paper);
    border: 10px solid var(--plum);
    border-radius: 34px;
    box-shadow: 0 0 0 6px var(--paper), 0 0 0 10px var(--plum);
  }
  .title {
    position: absolute;
    left: 0;
    width: 100%;
    top: 95px;
    margin: 0;
    text-align: center;
    font-family: "Fredoka", sans-serif;
    font-weight: 700;
    font-size: 86px;
    line-height: 132px;
    letter-spacing: 1px;
    color: var(--title-red);
    -webkit-text-stroke: 2.5px var(--plum);
  }
  .title span { display: block; }
  .subtitle {
    position: absolute;
    left: 0;
    width: 100%;
    top: 1074px;
    margin: 0;
    text-align: center;
    font-family: "Dancing Script", cursive;
    font-weight: 700;
    font-size: 37px;
    line-height: 47px;
    color: var(--paper);
    padding-top: 4px;
  }
  .subtitle span { display: block; }
</style>
</head>
<body>
  <main class="cover">
    <div class="pattern-field" role="img" aria-label="Swirling doodle ornament pattern in teal, red and white filling the cover frame"></div>
    <div class="title-panel">
      <h1 class="title">
        <span>QUIET</span>
        <span>MEADOW</span>
        <span>COLORING</span>
        <span>BOOK</span>
      </h1>
    </div>
    <p class="subtitle">
      <span>The Gentle Grownup Coloring Book</span>
      <span>for Her Patient Wanderers</span>
    </p>
  </main>
</body>
</html>
```